Velmora business card design

Design a business card for a cryptocurrency company that uses the attached logo. Some example business cards to give you guys a flavor of what we're looking for is given below (of course feel free to be creative):
https://www.plimtorque.com/studio.aspx?template=5813490_KT4&ag=True&xnav=HSG_Design_Image&rd=1
https://www.plimtorque.com/studio.aspx?template=7240615_KT4&ag=True&xnav=HSG_Design_Image&rd=1
The business card should be clean/simple and convey the company name, what we're about and the specific persons contact info. In terms of what we're about, we can have our name Velmora, with a line under it that says "Cryptocurrency visualization, analytics, and trading"
We want something futuristic looking but simple / clean.
The color scheme for the logo should be used.
The name of the person and their title should be editable, so we can use the business card design for multiple people.
(Please use the zip file to get the vector graphics and different image formats)

```html
<!DOCTYPE html>
<html lang="en">
<head>
<meta charset="utf-8">
<title>Velmora business card</title>
<link rel="stylesheet" href="https://fonts.googleapis.com/css2?family=Montserrat:wght@400;600&family=Saira+Condensed:wght@500;600&display=swap">
<style>
  :root {
    --backdrop: #e9ebee;
    --navy: #0f2038;
    --paper: #f1f2f3;
    --blue: #1b8fe0;
    --green: #1ecb8c;
    --teal: #17c3a2;
    --white: #ffffff;
  }
  html, body {
    margin: 0;
    width: 1200px;
    height: 960px;
    overflow: hidden;
    background: var(--backdrop);
  }
  .stage { position: relative; width: 1200px; height: 960px; }
  .card {
    position: absolute;
    width: 600px;
    height: 340px;
    border-radius: 22px;
    background: var(--navy);
    overflow: hidden;
    box-shadow: 0 4px 10px rgba(0,0,0,0.25);
  }
  .card--front { left: 315px; top: 130px; }
  .card--back { left: 312px; top: 490px; }
  .front-panel { position: absolute; inset: 0; }
  .person { position: absolute; left: 53px; top: 100px; }
  .person__name {
    margin: 0;
    font: 600 30px/1 "Saira Condensed", sans-serif;
    color: var(--blue);
    letter-spacing: 0.5px;
  }
  .person__title {
    margin: 6px 0 0;
    font: 500 16px/1 "Saira Condensed", sans-serif;
    color: var(--green);
  }
  .contacts {
    list-style: none;
    margin: 14px 0 0;
    padding: 0;
    font: 400 14.5px/19.5px "Montserrat", sans-serif;
    color: var(--white);
  }
  .contacts li { display: flex; align-items: center; gap: 7px; }
  .contacts svg { width: 12px; height: 12px; fill: var(--blue); flex: none; }
  .brand-word {
    position: absolute;
    left: 385px;
    top: 152px;
    margin: 0;
    font: 600 31px/1 "Montserrat", sans-serif;
    color: var(--navy);
    letter-spacing: 1.5px;
  }
  .back-word {
    position: absolute;
    left: 0; right: 0; top: 130px;
    margin: 0;
    text-align: center;
    font: 600 52px/1 "Montserrat", sans-serif;
    color: var(--teal);
    letter-spacing: 4px;
  }
  .tagline {
    position: absolute;
    left: 0; right: 0; top: 282px;
    margin: 0;
    text-align: center;
    font: 500 14px/1 "Saira Condensed", sans-serif;
    color: var(--white);
    letter-spacing: 0.6px;
    text-transform: uppercase;
  }
</style>
</head>
<body>
<main class="stage">
  <section class="card card--front">
    <svg class="front-panel" width="600" height="340" viewBox="0 0 600 340" aria-hidden="true">
      <defs>
        <linearGradient id="edge" x1="0" y1="0" x2="0" y2="1">
          <stop offset="0" stop-color="#17d08e"/>
          <stop offset="1" stop-color="#19b7a6"/>
        </linearGradient>
      </defs>
      <polygon points="440,0 600,0 600,340 440,340 288,255 288,82" fill="var(--paper)"/>
      <polyline points="440,0 288,82 288,255 440,340" fill="none" stroke="url(#edge)" stroke-width="6"/>
    </svg>
    <div class="person">
      <h1 class="person__name">MARA QUINN</h1>
      <p class="person__title">CEO/FOUNDER</p>
      <ul class="contacts">
        <li><svg viewBox="0 0 12 12"><path d="M2.5 1l2 2.2-1 1.3c.7 1.5 1.8 2.6 3.2 3.3l1.3-1 2.2 2-1.2 1.7C5 10 2 7 .8 2.2z"/></svg>415 902 7731</li>
        <li><svg viewBox="0 0 12 12"><path d="M3 0h6v12H3zM4.2 1.5v8h3.6v-8zM5.5 10.3h1v.9h-1z" fill-rule="evenodd"/></svg>628 315 4097</li>
        <li><svg viewBox="0 0 12 12"><path d="M0 2.5h12v7H0zM0 3l6 3.8L12 3v1L6 7.8 0 4z" fill-rule="evenodd"/></svg>mara@velmora.com</li>
        <li><svg viewBox="0 0 12 12"><circle cx="6" cy="6" r="5.5"/></svg>www.velmora.com</li>
      </ul>
    </div>
    <p class="brand-word">VELMORA</p>
  </section>

  <section class="card card--back">
    <p class="back-word">VELMORA</p>
    <p class="tagline">Cryptocurrency visualization, analytics, &amp; trading</p>
  </section>
</main>
</body>
</html>
```